Events & Entertainment Production Coordination Business Cards

We need a business card for a new company based in Los Angeles called "Bright Stage Works"
Our company brings people together for events and helps coordinate different productions. We bring artists from a different country to perform or do events in the U.S.
We are looking for something fun, lively, colorful, creative, and simple.
Nothing that looks too crisp, dark, stiff, or modern.
We connect people from different parts of the world, so definitely something eye-catching will be great!
Colors we would like to see are Black, Yellow, Red, White, Brown to name a few. (Feel free to use more!)
(Double-sided is an option also)
Industry/Entity Type
Business
Contact Information for Business Card
Contact Information to put on Business Card:
Name
Title
Address - 2 lines
Phone - place for 3 numbers
E-mail
URL
Look and feel

```html
<!DOCTYPE html>
<html lang="en">
<head>
<meta charset="utf-8">
<title>Bright Stage Works – Business Cards</title>
<link href="https://fonts.googleapis.com/css2?family=Montserrat:wght@700&family=Open+Sans:wght@400;600;700&display=swap" rel="stylesheet">
<style>
  :root {
    --stage-bg: #ece7df;
    --card-yellow: #f7c531;
    --card-cream: #fff6df;
    --ink-brown: #3a2216;
    --ink-black: #1a1210;
    --accent-red: #e0352b;
    --soft-yellow: #f9d766;
    --detail-brown: #4a3326;
  }
  * { margin: 0; padding: 0; box-sizing: border-box; }
  html, body { width: 1200px; height: 900px; overflow: hidden; }
  body {
    background: var(--stage-bg);
    font-family: "Open Sans", Arial, sans-serif;
    position: relative;
  }
  .card {
    position: absolute;
    left: 285px;
    width: 630px;
    height: 360px;
    border-radius: 26px;
    overflow: hidden;
    box-shadow: 0 10px 30px rgba(58,34,22,0.22);
  }
  .card--front { top: 60px; background: var(--card-yellow); }
  .card--back { top: 480px; background: var(--card-cream); }
  .brand-name {
    font-family: "Montserrat", Arial, sans-serif;
    font-weight: 700;
    color: var(--ink-brown);
    text-transform: uppercase;
    letter-spacing: 1px;
    white-space: nowrap;
  }
  .card--front .brand-name {
    position: absolute;
    left: 0; right: 0;
    top: 158px;
    text-align: center;
    font-size: 36px;
  }
  .card--back .brand-name {
    position: absolute;
    left: 42px;
    top: 78px;
    font-size: 34px;
    line-height: 1.2;
  }
  .backdrop-circle {
    position: absolute;
    left: 395px;
    top: 30px;
    width: 290px;
    height: 290px;
    border-radius: 50%;
    border: 18px solid var(--soft-yellow);
  }
  .divider {
    position: absolute;
    left: 118px;
    right: 0;
    top: 230px;
    height: 2px;
    background: var(--accent-red);
  }
  .person {
    position: absolute;
    left: 62px;
    top: 136px;
  }
  .person__name {
    font-family: "Montserrat", Arial, sans-serif;
    font-weight: 700;
    font-size: 22px;
    color: var(--accent-red);
    text-transform: uppercase;
    line-height: 1.15;
  }
  .person__title {
    font-size: 13px;
    font-weight: 600;
    color: var(--ink-black);
    letter-spacing: 0.5px;
    margin-left: 18px;
    line-height: 1.4;
  }
  .address {
    position: absolute;
    left: 98px;
    top: 182px;
    font-size: 13px;
    line-height: 1.35;
    color: var(--detail-brown);
  }
  .contacts {
    position: absolute;
    left: 128px;
    top: 240px;
    list-style: none;
  }
  .contacts li {
    display: flex;
    align-items: center;
    gap: 10px;
    font-size: 13px;
    line-height: 19px;
    color: var(--detail-brown);
  }
  .contacts svg { width: 11px; height: 11px; flex: none; }
</style>
</head>
<body>
  <section class="card card--front">
    <h1 class="brand-name">Bright Stage Works</h1>
  </section>

  <section class="card card--back">
    <div class="backdrop-circle"></div>
    <div class="divider"></div>
    <h2 class="brand-name">Bright Stage Works</h2>
    <div class="person">
      <div class="person__name">Marco Delano</div>
      <div class="person__title">DIRECTOR</div>
    </div>
    <div class="address">
      14 - 20 Harbor Lane St<br>
      Westfield Park 2041 Australia
    </div>
    <ul class="contacts">
      <li>
        <svg viewBox="0 0 12 12"><path d="M2 1l2.5 0 1 3-1.5 1c.6 1.3 1.7 2.4 3 3l1-1.5 3 1V11C5.5 11 1 6.5 1 2z" fill="#e0352b"/></svg>
        +330 2190-4470
      </li>
      <li>
        <svg viewBox="0 0 12 12"><rect x="3" y="0.5" width="6" height="11" rx="1" fill="none" stroke="#e0352b" stroke-width="1.4"/><circle cx="6" cy="9.5" r="0.8" fill="#e0352b"/></svg>
        +330 6815-3027
      </li>
      <li>
        <svg viewBox="0 0 12 12"><rect x="1" y="4" width="10" height="7" rx="1" fill="#e0352b"/><rect x="3" y="1" width="6" height="3" fill="#e0352b"/></svg>
        +330 5372-9164
      </li>
      <li>
        <svg viewBox="0 0 12 12"><rect x="0.8" y="2" width="10.4" height="8" rx="1" fill="none" stroke="#e0352b" stroke-width="1.3"/><path d="M1 2.5l5 4 5-4" fill="none" stroke="#e0352b" stroke-width="1.3"/></svg>
        info@brightstageworks.com
      </li>
      <li>
        <svg viewBox="0 0 12 12"><circle cx="6" cy="6" r="5.3" fill="#e0352b"/><path d="M1 6h10M6 0.7c-2.5 3-2.5 7.6 0 10.6M6 0.7c2.5 3 2.5 7.6 0 10.6" fill="none" stroke="#fff6df" stroke-width="0.8"/></svg>
        www.brightstageworks.com
      </li>
    </ul>
  </section>
</body>
</html>
```